Business Card Design for a Marketing Agency

I will need a business card design for a new marketing agency based in Singapore. We provide marketing and sales solutions to our startup companies. We would like to see the designs to be creative and client friendly. It should display contrast, creative and simple. see: tavrelomarketing.com

For the back part please list out all the work done by the company listed in the website

```html
<!DOCTYPE html>
<html lang="en">
<head>
<meta charset="utf-8">
<title>Tavrelo Marketing – Business Card</title>
<link href="https://fonts.googleapis.com/css2?family=Titillium+Web:wght@400;600;700&family=Exo+2:wght@700&display=swap" rel="stylesheet">
<style>
  :root {
    --page: #2a2a2c;
    --teal: #1f7d76;
    --teal-light: #2a9a90;
    --yellow: #e6b422;
    --dark: #2c2c2c;
    --ink: #f2f2f2;
    --muted: #d8d8d8;
    --navy-top: #2a4256;
    --navy-bottom: #1c2b3a;
    --arrow: #35b3a8;
  }
  * { box-sizing: border-box; margin: 0; padding: 0; }
  html, body { width: 901px; height: 1200px; overflow: hidden; }
  body {
    background: var(--page);
    font-family: "Titillium Web", Arial, sans-serif;
    color: var(--ink);
    position: relative;
  }
  .card {
    position: absolute;
    left: 130px;
    width: 640px;
    height: 366px;
    overflow: hidden;
    box-shadow: 0 10px 24px rgba(0,0,0,.45);
  }
  .card--front { top: 100px; background: var(--dark); }
  .card--back {
    top: 720px;
    background: linear-gradient(160deg, var(--navy-top), var(--navy-bottom));
  }

  /* front */
  .brand-band {
    position: absolute; left: 0; top: 0; width: 640px; height: 130px;
    background: linear-gradient(180deg, var(--teal-light), var(--teal));
  }
  .brand-name {
    position: absolute; left: 110px; top: 14px;
    font-size: 44px; font-weight: 700; color: var(--muted); letter-spacing: 1px;
    white-space: nowrap; line-height: 1.2;
  }
  .brand-tagline {
    position: absolute; left: 170px; top: 66px;
    font-size: 13px; letter-spacing: 3px; color: var(--muted); white-space: nowrap;
  }
  .row {
    position: absolute; display: flex; align-items: center; gap: 14px;
    font-size: 17px; color: var(--ink); padding: 0 16px; white-space: nowrap;
  }
  .row--yellow { background: var(--yellow); }
  .row--dark { background: var(--dark); }
  .row--left { left: 0; width: 380px; }
  .row--right { left: 380px; width: 260px; justify-content: space-between; font-size: 16px; }
  .icon { width: 22px; height: 22px; flex: none; }
  .dot { width: 18px; height: 18px; border-radius: 50%; background: var(--ink); flex: none; }

  /* back */
  .services { position: absolute; left: 0; top: 58px; list-style: none; }
  .service {
    height: 32px; margin-bottom: 6px; background: var(--yellow);
    font-family: "Exo 2", Arial, sans-serif; font-weight: 700; font-size: 20px;
    color: var(--ink); text-align: right; padding-right: 12px; line-height: 32px;
    white-space: nowrap;
  }
  .growth-artwork {
    position: absolute; left: 400px; top: 70px; width: 170px; height: 150px;
    border-radius: 8px;
    background: linear-gradient(135deg, var(--yellow) 0%, var(--yellow) 45%, var(--arrow) 100%);
    opacity: .85;
  }
</style>
</head>
<body>

<section class="card card--front" aria-label="Business card front">
  <div class="brand-band">
    <div class="brand-name">Tavrelo Marketing</div>
    <div class="brand-tagline">Marketing &amp; Sales Professional</div>
  </div>

  <div class="row row--right row--dark" style="top:88px;height:56px">feed: @tavrelo.m <span class="dot"></span></div>
  <div class="row row--right row--yellow" style="top:144px;height:56px">page: /tavrelo.m <span class="dot"></span></div>
  <div class="row row--right row--dark" style="top:200px;height:56px">circle: /tavrelo.m <span class="dot"></span></div>
  <div class="row row--right row--yellow" style="top:256px;height:56px">42 Lorong Tembu 318720
    <svg class="icon" viewBox="0 0 24 24"><path d="M12 2a7 7 0 0 0-7 7c0 5 7 13 7 13s7-8 7-13a7 7 0 0 0-7-7zm0 9.5A2.5 2.5 0 1 1 12 6.5a2.5 2.5 0 0 1 0 5z" fill="#f2f2f2"/></svg>
  </div>

  <div class="row row--left row--yellow" style="top:130px;height:52px">
    <svg class="icon" viewBox="0 0 24 24"><rect x="2" y="5" width="20" height="14" fill="none" stroke="#f2f2f2" stroke-width="2"/><path d="M2 5l10 8 10-8" fill="none" stroke="#f2f2f2" stroke-width="2"/></svg>
    sales@tavrelomarketing.com
  </div>
  <div class="row row--left row--dark" style="top:182px;height:52px">
    <svg class="icon" viewBox="0 0 24 24"><circle cx="12" cy="12" r="10" fill="#bdbdbd"/><path d="M2 12h20M12 2c4 4 4 16 0 20M12 2c-4 4-4 16 0 20" fill="none" stroke="#2c2c2c" stroke-width="1.5"/></svg>
    www.tavrelomarketing.com
  </div>
  <div class="row row--left row--yellow" style="top:234px;height:52px">
    <svg class="icon" viewBox="0 0 24 24"><rect x="6" y="2" width="12" height="20" rx="2" fill="none" stroke="#f2f2f2" stroke-width="2"/><circle cx="12" cy="18" r="1.2" fill="#f2f2f2"/></svg>
    +65 81470359
  </div>
  <div class="row row--left row--dark" style="top:286px;height:80px">
    <svg class="icon" viewBox="0 0 24 24"><path d="M3 9c0-3 4-5 9-5s9 2 9 5v2h-5V8H8v3H3z" fill="#cfcfcf"/><rect x="5" y="12" width="14" height="9" rx="1" fill="#cfcfcf"/></svg>
    +65 81470359
  </div>
</section>

<section class="card card--back" aria-label="Business card back">
  <ul class="services">
    <li class="service" style="width:210px">Telemarketing</li>
    <li class="service" style="width:225px">Web Design</li>
    <li class="service" style="width:240px">Content Writing</li>
    <li class="service" style="width:255px">E-mail</li>
    <li class="service" style="width:270px">Social</li>
    <li class="service" style="width:285px">SEO</li>
    <li class="service" style="width:300px">Market Research</li>
  </ul>
  <div class="growth-artwork" role="img" aria-label="Illustration of a mobile device with a rising growth arrow"></div>
</section>

</body>
</html>
```